Larchmont Vale Rehab and Wellness Postcard

This is a postcard for our chiropractic office, to raise awareness of our practice. Please refer to our grand opening flyer for contact information and logo. Please include the following:
Larchmont Vale Rehab and Wellness
Chiropractic & Wellness
Spinal Correction
Injury Rehabilitation
Tired of living with Fatigue, Allergies, High/Low Blood Pressure, Headaches, Numbness/Tingling in Hands/Feet, Frequent Infection, Back Pain, Neck Pain or ANY Other Health Problems?
Call Today for a Free Consultation with the Doctor!
(Space is Limited, Please Call to Reserve)

```html
<!DOCTYPE html>
<html lang="en">
<head>
<meta charset="utf-8">
<title>Larchmont Vale Rehab and Wellness Postcard</title>
<link rel="stylesheet" href="https://fonts.googleapis.com/css2?family=Fira+Sans:wght@700;800&family=Open+Sans:wght@400;600;700&family=Sniglet&display=swap">
<style>
  :root {
    --bg: #6e6e6e;
    --blue: #1e6fbd;
    --navy: #0d2b48;
    --white: #ffffff;
    --logo-blue: #2c6fb3;
    --line: #3a3a3a;
    --map-grey: #e4e4e4;
  }
  * { box-sizing: border-box; margin: 0; padding: 0; }
  html, body { width: 880px; height: 1200px; overflow: hidden; }
  body { background: var(--bg); font-family: "Open Sans", sans-serif; position: relative; }

  .card { position: absolute; overflow: hidden; background: var(--white); }

  /* Front side */
  .front { left: 51px; top: 58px; width: 773px; height: 526px; background: var(--blue); }
  .front-band { position: absolute; left: 0; top: 190px; width: 773px; height: 166px; background: var(--navy); }
  .front-visual {
    position: absolute; left: 480px; top: 0; width: 293px; height: 526px;
    background:
      radial-gradient(ellipse 70% 60% at 45% 55%, rgba(232,150,80,0.55), rgba(232,150,80,0) 70%),
      linear-gradient(90deg, #d9d9d9 0%, #f2f2f2 55%, #bdbdbd 100%);
  }
  .service-list { position: absolute; left: 40px; top: 34px; list-style: none; }
  .service-list li {
    position: relative; padding-left: 37px;
    font-family: "Fira Sans", sans-serif; font-weight: 800; color: var(--white);
    font-size: 29px; line-height: 33px; letter-spacing: 0.3px; margin-bottom: 6px;
  }
  .service-list li::before {
    content: ""; position: absolute; left: 2px; top: 9px; width: 16px; height: 16px;
    border: 2px solid var(--white); border-radius: 50%; opacity: 0.85;
  }
  .symptoms {
    position: absolute; left: 40px; top: 204px; white-space: nowrap;
    color: var(--white); font-size: 19.5px; line-height: 27px; font-weight: 400;
  }
  .symptoms strong { font-weight: 700; }
  .cta { position: absolute; left: 40px; top: 364px; color: var(--white); }
  .cta-title { font-family: "Fira Sans", sans-serif; font-weight: 800; font-size: 43px; line-height: 46px; letter-spacing: 0.5px; }
  .cta-sub { font-family: "Fira Sans", sans-serif; font-weight: 800; font-size: 28px; line-height: 32px; white-space: nowrap; }
  .cta-sub small { font-size: 17px; }
  .cta-phone { display: flex; align-items: center; gap: 12px; margin-top: 6px; font-family: "Fira Sans", sans-serif; font-weight: 800; font-size: 40px; line-height: 44px; }
  .cta-note { font-size: 14.5px; margin-top: 4px; }

  .brand {
    position: absolute; font-family: "Sniglet", sans-serif; color: var(--logo-blue);
    font-size: 21px; line-height: 24px; letter-spacing: 1.5px; text-align: center;
    display: flex; flex-direction: column; align-items: center; gap: 6px;
  }
  .brand-dot { width: 34px; height: 34px; border-radius: 50%; background: var(--logo-blue); }
  .front .brand { left: 546px; top: 46px; width: 200px; }

  /* Back side */
  .back { left: 56px; top: 622px; width: 768px; height: 522px; }
  .back-art { position: absolute; inset: 0; }
  .office { position: absolute; left: 39px; top: 263px; color: var(--white); }
  .office-title { font-size: 25px; font-weight: 400; line-height: 30px; }
  .office-title b { font-weight: 700; }
  .office-rule { width: 28px; height: 3px; background: var(--white); margin: 5px 0 10px; }
  .office-row { display: flex; align-items: flex-start; gap: 8px; font-size: 14.5px; line-height: 19px; margin-bottom: 8px; }
  .office-row svg { flex: none; margin-top: 2px; }
  .office-row.inline { gap: 24px; }
  .office-row .pair { display: flex; align-items: center; gap: 6px; }
  .office-row .strong { font-weight: 700; }
  .serving { position: absolute; left: 39px; top: 456px; color: var(--white); font-size: 12.5px; line-height: 18px; }
  .serving b { font-weight: 700; }
  .serving span { color: #d4dbe4; }
  .back .brand { left: 410px; top: 42px; width: 210px; }
  .stamp-box { position: absolute; left: 632px; top: 38px; width: 92px; height: 90px; border: 1px solid #555; }
  .address-line { position: absolute; left: 528px; width: 196px; height: 1px; background: var(--line); }
</style>
</head>
<body>

<section class="card front" aria-label="Postcard front">
  <div class="front-band"></div>
  <div class="front-visual" role="img" aria-label="Illustration of a human spine with glowing discs"></div>

  <ul class="service-list">
    <li>CHIROPRACTIC &amp;<br>WELLNESS</li>
    <li>SPINAL CORRECTION</li>
    <li>INJURY REHABILITATION</li>
  </ul>

  <p class="symptoms">Tired of living with Fatigue, Allergies,<br>High/Low Blood Pressure, Headaches,<br>Numbness/Tingling in Hands/Feet,<br>Frequent Infection, Back Pain, Neck Pain or<br>ANY Other <strong>Health Problems?</strong></p>

  <div class="cta">
    <p class="cta-title">CALL TODAY</p>
    <p class="cta-sub">for a Free Consultation <small>with the Doctor!</small></p>
    <p class="cta-phone">
      <svg width="30" height="30" viewBox="0 0 30 30" aria-hidden="true"><circle cx="15" cy="15" r="13.5" fill="none" stroke="#fff" stroke-width="2.4"/><path d="M10 8.5 l3 0 l1.2 4 l-2 1.5 c1 2.2 2.5 3.7 4.6 4.6 l1.5-2 l4 1.2 l0 3 c-7 .5-12.8-5.3-12.3-12.3z" fill="#fff"/></svg>
      555-014-3200
    </p>
    <p class="cta-note">(Space is Limited, Please Call to Reserve)</p>
  </div>

  <div class="brand"><span class="brand-dot"></span>Larchmont Vale Rehab</div>
</section>

<section class="card back" aria-label="Postcard back">
  <svg class="back-art" width="768" height="522" viewBox="0 0 768 522">
    <defs>
      <linearGradient id="studio" x1="0" y1="0" x2="0" y2="1">
        <stop offset="0" stop-color="#eef1f4"/>
        <stop offset="0.6" stop-color="#d6d9dc"/>
        <stop offset="1" stop-color="#9fb7cf"/>
      </linearGradient>
      <clipPath id="photoClip"><path d="M0 0 L300 0 C375 50 395 150 388 240 L0 240 Z"/></clipPath>
    </defs>
    <path d="M0 0 L322 0 C450 80 470 300 380 440 C350 485 310 510 276 522 L0 522 Z" fill="var(--blue)"/>
    <path d="M300 0 C385 55 405 160 396 250" fill="none" stroke="#a9a9a9" stroke-width="8"/>
    <rect role="img" aria-label="Photo of a group doing a stretching class on mats" x="0" y="0" width="400" height="240" fill="url(#studio)" clip-path="url(#photoClip)"/>
    <path d="M0 438 L352 438 C330 475 305 505 276 522 L0 522 Z" fill="var(--navy)"/>
    <circle cx="358" cy="306" r="94" fill="var(--navy)"/>
    <circle role="img" aria-label="Street map showing the office location" cx="352" cy="306" r="84" fill="var(--map-grey)"/>
  </svg>

  <div class="office">
    <p class="office-title">Our <b>office</b></p>
    <div class="office-rule"></div>
    <div class="office-row">
      <svg width="11" height="15" viewBox="0 0 11 15" aria-hidden="true"><circle cx="5.5" cy="5" r="3.5" fill="none" stroke="#fff" stroke-width="1.4"/><path d="M5.5 8.5 V13 M2 13.5 H9" stroke="#fff" stroke-width="1.4"/></svg>
      <span>Larchmont Vale Rehab<br>418 Orchard Street, Suite 140<br>Larchmont Vale, NJ 07990</span>
    </div>
    <div class="office-row">
      <svg width="12" height="12" viewBox="0 0 12 12" aria-hidden="true"><rect x="0.7" y="2" width="10.6" height="8" fill="none" stroke="#fff" stroke-width="1.2"/><path d="M1 2.5 L6 6.5 L11 2.5" fill="none" stroke="#fff" stroke-width="1.2"/></svg>
      <span>info@lvrehab.com</span>
    </div>
    <div class="office-row inline">
      <span class="pair"><svg width="12" height="12" viewBox="0 0 30 30" aria-hidden="true"><circle cx="15" cy="15" r="13" fill="none" stroke="#fff" stroke-width="3"/><path d="M10 8.5 l3 0 l1.2 4 l-2 1.5 c1 2.2 2.5 3.7 4.6 4.6 l1.5-2 l4 1.2 l0 3 c-7 .5-12.8-5.3-12.3-12.3z" fill="#fff"/></svg><span class="strong">555-014-3200</span></span>
      <span class="pair"><svg width="12" height="12" viewBox="0 0 12 12" aria-hidden="true"><circle cx="6" cy="6" r="5.2" fill="none" stroke="#fff" stroke-width="1.1"/><ellipse cx="6" cy="6" rx="2.3" ry="5.2" fill="none" stroke="#fff" stroke-width="1"/><path d="M0.8 6 H11.2" stroke="#fff" stroke-width="1"/></svg><span>www.lvrehab.com</span></span>
    </div>
  </div>

  <p class="serving"><b>Proudly Serving:</b><br><span>Larchmont Vale, Elm Ridge, Cedar Falls,<br>Brookhaven and the greater Vale County</span></p>

  <div class="brand"><span class="brand-dot"></span>Larchmont Vale Rehab</div>
  <div class="stamp-box"></div>
  <div class="address-line" style="top:279px"></div>
  <div class="address-line" style="top:326px"></div>
  <div class="address-line" style="top:371px"></div>
</section>

</body>
</html>
```